Health care technology software systems

We have a solid logo. We have company colors that will need to be used as well. We just need a great business card design. We sell to health plans but want to be modern
Updates

Need extra days to review

Target Market(s)

Health technology sector selling into Health Plans

Industry/Entity Type

Health Care Technology

Contact Information for Business Card

Name, title, address, phone number, email

Requirements
Must have
• Use of Kembrata corporate colors - Uploaded w/ our logos

```html
<!DOCTYPE html>
<html lang="en">
<head>
<meta charset="utf-8">
<title>Kembrata Business Card</title>
<link href="https://fonts.googleapis.com/css2?family=Montserrat:wght@300;400;500&display=swap" rel="stylesheet">
<style>
  :root {
    --navy: #3a4f9e;
    --green: #8bc53f;
    --sky: #2fa8df;
    --ink: #1d1d1d;
    --charcoal: #3a3a3a;
    --paper: #ffffff;
    --night: #000000;
    --backdrop: #2b2b2b;
  }
  * { box-sizing: border-box; margin: 0; padding: 0; }
  html, body {
    width: 1200px; height: 780px; overflow: hidden;
    background: var(--backdrop);
    font-family: "Montserrat", sans-serif;
  }
  .canvas {
    width: 1200px; height: 780px;
    display: flex; align-items: center; justify-content: center; gap: 40px;
  }
  .card {
    position: relative;
    width: 540px; height: 310px;
    border-radius: 28px;
    overflow: hidden;
    background: var(--paper);
    box-shadow: 0 14px 30px rgba(0,0,0,.45);
  }
  .card-art { position: absolute; inset: 0; width: 100%; height: 100%; }

  .brand { position: absolute; display: flex; align-items: center; }
  .brand-dot { border-radius: 50%; background: var(--sky); flex: none; }
  .brand-name { font-weight: 300; letter-spacing: .01em; line-height: 1; }

  .card-front .brand { left: 50%; top: 50%; transform: translate(-50%, -30%); gap: 20px; }
  .card-front .brand-dot { width: 44px; height: 44px; }
  .card-front .brand-name { font-size: 58px; color: var(--charcoal); }

  .card-back .brand { left: 34px; bottom: 34px; gap: 12px; }
  .card-back .brand-dot { width: 24px; height: 24px; }
  .card-back .brand-name { font-size: 30px; color: var(--paper); }

  .identity { position: absolute; right: 34px; top: 32px; text-align: right; color: var(--ink); }
  .identity-name { font-size: 26px; font-weight: 400; letter-spacing: .03em; }
  .identity-title { font-size: 11px; font-weight: 400; margin-top: 3px; letter-spacing: .03em; }

  .contacts { position: absolute; right: 30px; top: 118px; list-style: none; color: var(--ink); }
  .contact {
    display: flex; justify-content: flex-end; align-items: flex-start; gap: 8px;
    font-size: 10.5px; line-height: 1.35; margin-bottom: 9px; text-align: right;
  }
  .contact-icon { width: 12px; height: 12px; flex: none; fill: var(--ink); margin-top: 1px; }
  .contact-icon--outline { fill: none; stroke: var(--ink); stroke-width: 2; }
</style>
</head>
<body>
<main class="canvas">

  <section class="card card-front" aria-label="Card front">
    <svg class="card-art" viewBox="0 0 540 310" role="img" aria-label="Soft brand-colour accent area in the top corner">
      <defs>
        <linearGradient id="front-accent" x1="0" y1="1" x2="1" y2="0">
          <stop offset="0" stop-color="var(--navy)" stop-opacity=".55"/>
          <stop offset=".5" stop-color="var(--green)" stop-opacity=".55"/>
          <stop offset="1" stop-color="var(--sky)" stop-opacity=".55"/>
        </linearGradient>
      </defs>
      <ellipse cx="480" cy="-140" rx="300" ry="200" fill="url(#front-accent)"/>
      <ellipse cx="480" cy="-140" rx="262" ry="162" fill="var(--paper)"/>
    </svg>
    <div class="brand">
      <span class="brand-dot"></span>
      <span class="brand-name">kembrata</span>
    </div>
  </section>

  <section class="card card-back" aria-label="Card back">
    <svg class="card-art" viewBox="0 0 540 310" role="img" aria-label="Soft brand-colour accent area dividing the dark and light sides">
      <defs>
        <linearGradient id="back-accent" x1="0" y1="1" x2="1" y2="0">
          <stop offset="0" stop-color="var(--navy)"/>
          <stop offset=".5" stop-color="var(--green)"/>
          <stop offset="1" stop-color="var(--sky)"/>
        </linearGradient>
      </defs>
      <rect width="540" height="310" fill="var(--night)"/>
      <ellipse cx="560" cy="20" rx="400" ry="300" fill="url(#back-accent)" opacity=".85"/>
      <ellipse cx="560" cy="20" rx="360" ry="262" fill="var(--paper)"/>
    </svg>

    <header class="identity">
      <h1 class="identity-name">Daniel Marsh</h1>
      <p class="identity-title">Managing Director</p>
    </header>

    <ul class="contacts">
      <li class="contact">
        <span>+1 555 010 2244</span>
        <svg class="contact-icon" viewBox="0 0 24 24"><path d="M6.6 10.8a15.1 15.1 0 0 0 6.6 6.6l2.2-2.2c.3-.3.7-.4 1-.2 1.1.4 2.3.6 3.6.6.6 0 1 .4 1 1V20c0 .6-.4 1-1 1C10.6 21 3 13.4 3 4c0-.6.4-1 1-1h3.5c.6 0 1 .4 1 1 0 1.3.2 2.5.6 3.6.1.3 0 .7-.2 1z"/></svg>
      </li>
      <li class="contact">
        <span>mail address@kembrata.com</span>
        <svg class="contact-icon contact-icon--outline" viewBox="0 0 24 24"><path d="M2 5h20v14H2z M3.5 6.5 12 13l8.5-6.5"/></svg>
      </li>
      <li class="contact">
        <span>www.kembrata.com</span>
        <svg class="contact-icon contact-icon--outline" viewBox="0 0 24 24"><circle cx="12" cy="12" r="10"/><path d="M2 12h20M12 2c3 3 3 17 0 20M12 2c-3 3-3 17 0 20"/></svg>
      </li>
      <li class="contact">
        <span>420 ALDER LANE 210<br>Riverton, Oregon 97000, US</span>
        <svg class="contact-icon" viewBox="0 0 24 24"><path d="M12 2a7 7 0 0 0-7 7c0 5 7 13 7 13s7-8 7-13a7 7 0 0 0-7-7zm0 9.5A2.5 2.5 0 1 1 12 6.5a2.5 2.5 0 0 1 0 5z"/></svg>
      </li>
    </ul>

    <div class="brand">
      <span class="brand-dot"></span>
      <span class="brand-name">kembrata</span>
    </div>
  </section>

</main>
</body>
</html>
```